Bref créative
KEL Papeterie
I need double sided standard sized Business Card [3.5" x 2"]
At the discretion of the artist
Professional
First & Last Name
Title
Address
Toll Free
Phone
Cell
Fax
Email@kelvu.org
Web Address
The contact information requested above is private, please put generic information in the design for each category.
Logo and website address
Please let us know if you need another format of the logo.

```html
<!DOCTYPE html>
<html lang="fr">
<head>
<meta charset="utf-8">
<title>KEL Papeterie – Stationery Set</title>
<link href="https://fonts.googleapis.com/css2?family=Questrial&display=swap" rel="stylesheet">
<style>
  :root{
    --orange:#fbb61f;
    --orange-deep:#f5a00f;
    --orange-light:#fdd063;
    --paper:#ffffff;
    --ink:#2f6fa6;
    --ink-light:#4aa3dc;
    --bg:#ffffff;
  }
  *{margin:0;padding:0;box-sizing:border-box}
  html,body{width:1200px;height:925px;overflow:hidden;background:var(--bg)}
  body{position:relative;font-family:"Questrial",sans-serif}
  .block{position:absolute}
  .orange{background:var(--orange)}
  .pattern{background:radial-gradient(circle at 70% 30%,var(--orange-light) 0,var(--orange) 45%,var(--orange-deep) 100%)}
  .white{background:var(--paper)}
  .brand{display:flex;align-items:center;gap:5px;font-weight:400;color:var(--ink);font-size:15px;letter-spacing:1px}
  .brand .dot{width:12px;height:12px;border-radius:50%;background:var(--ink)}
  .contact{position:absolute;font-size:8.5px;line-height:11.5px;color:var(--ink-light);letter-spacing:.6px}
  .contact .name{color:var(--ink);font-size:10px;letter-spacing:1px}
  .contact.on-orange,.contact.on-orange .name{color:var(--paper)}
  .vertical{transform:rotate(-90deg)}
</style>
</head>
<body>

<!-- Letterhead -->
<section class="letterhead">
  <div class="block pattern" style="left:89px;top:84px;width:480px;height:139px" role="img" aria-label="Decorative orange citrus circles"></div>
  <div class="contact on-orange" style="left:108px;top:104px">
    <div class="name">Marco Lefevre<br>Creative Manager</div>
    14 Rue Verte, Lyon<br>Toll Free: 800 555 0142<br>Phone: 0555 010 234<br>Cell: 0555 010 876<br>Mail: Email@kelvu.org<br>Web: www.kelvu.org
  </div>
  <div class="block white" style="left:89px;top:223px;width:480px;height:53px;display:flex;align-items:center;justify-content:center">
    <div class="brand"><span class="dot"></span>KEL</div>
  </div>
  <div class="block pattern" style="left:89px;top:276px;width:480px;height:509px" role="img" aria-label="Decorative orange citrus circles"></div>
</section>

<!-- Business card front -->
<section class="card-front">
  <div class="block orange" style="left:617px;top:223px;width:60px;height:120px;display:flex;align-items:center;justify-content:center">
    <div class="brand vertical"><span class="dot"></span>KEL</div>
  </div>
  <div class="block white" style="left:677px;top:223px;width:120px;height:120px;border:1px solid #f2f2f2"></div>
  <div class="contact" style="left:686px;top:232px;font-size:7.5px;line-height:10px">
    <div class="name" style="font-size:8.5px">Marco Lefevre<br>Creative Manager</div>
    14 Rue Verte, Lyon<br>Toll Free: 800 555 0142<br>Phone: 0555 010 234<br>Cell: 0555 010 876<br>Mail: Email@kelvu.org<br>Web: www.kelvu.org
  </div>
</section>

<!-- Business card backs -->
<section class="card-backs">
  <div class="block orange" style="left:806px;top:223px;width:24px;height:120px"></div>
  <div class="block pattern" style="left:840px;top:223px;width:84px;height:120px" role="img" aria-label="Decorative orange citrus circles"></div>
  <div class="block white" style="left:924px;top:223px;width:52px;height:120px;display:flex;align-items:center;justify-content:center">
    <div class="brand" style="font-size:12px"><span class="dot" style="width:9px;height:9px"></span>KEL</div>
  </div>
  <div class="block pattern" style="left:979px;top:223px;width:82px;height:120px" role="img" aria-label="Decorative orange citrus circles"></div>
</section>

<!-- Envelope -->
<section class="envelope">
  <div class="block orange" style="left:617px;top:473px;width:480px;height:67px"></div>
  <div class="block white" style="left:660px;top:473px;width:53px;height:67px;display:flex;align-items:center;justify-content:center">
    <div class="brand" style="font-size:12px;transform:rotate(180deg)"><span class="dot" style="width:9px;height:9px"></span>KEL</div>
  </div>
  <div class="block orange" style="left:617px;top:540px;width:43px;height:245px"></div>
  <div class="block white" style="left:660px;top:540px;width:53px;height:245px;display:flex;align-items:center;justify-content:center">
    <div class="brand" style="font-size:12px"><span class="dot" style="width:9px;height:9px"></span>KEL</div>
  </div>
  <div class="block pattern" style="left:713px;top:540px;width:384px;height:245px" role="img" aria-label="Decorative orange citrus circles"></div>
  <div class="block white" style="left:713px;top:630px;width:150px;height:120px"></div>
  <div class="contact" style="left:733px;top:650px">
    <div class="name">Marco Lefevre<br>Creative Manager</div>
    14 Rue Verte, Lyon<br>Toll Free: 800 555 0142<br>Phone: 0555 010 234<br>Cell: 0555 010 876<br>Mail: Email@kelvu.org<br>Web: www.kelvu.org
  </div>
</section>

</body>
</html>
```